Need DL Flyer for Real Estate Drops

We need a real estate flyer ,double sided. With content on 1 side like: Want to know what's your house is worth " contact us today and on other side agent details. We are looking for an ongoing partnership with designer so this assignment will be ongoing

```html
<!DOCTYPE html>
<html lang="en">
<head>
<meta charset="UTF-8">
<title>Dunehill Real Estate – What's Your House Worth</title>
<link href="https://fonts.googleapis.com/css2?family=Anton&display=swap" rel="stylesheet">
<style>
  :root {
    --navy: #08102f;
    --brand-red: #cc0a0a;
    --white: #ffffff;
    --house-grey: #dfe5e6;
    --buy-red: #e8203a;
    --sell-blue: #4bb4ee;
  }
  * { margin: 0; padding: 0; box-sizing: border-box; }
  html, body {
    width: 1200px;
    height: 2400px;
    overflow: hidden;
    background: var(--navy);
  }
  .flyer {
    position: relative;
    width: 1200px;
    height: 2400px;
    background: var(--navy);
    font-family: 'Anton', 'Impact', sans-serif;
    color: var(--white);
  }
  .brand {
    position: absolute;
    top: 213px;
    left: 150px;
    display: flex;
    align-items: center;
    gap: 70px;
  }
  .brand-square {
    width: 262px;
    height: 262px;
    background: var(--brand-red);
  }
  .brand-name {
    display: flex;
    flex-direction: column;
    align-items: center;
    line-height: 1;
  }
  .brand-name .name {
    font-size: 150px;
    letter-spacing: 2px;
  }
  .brand-name .tagline {
    margin-top: 14px;
    font-size: 44px;
    letter-spacing: 10px;
  }
  .headline {
    position: absolute;
    top: 600px;
    left: 0;
    width: 100%;
    text-align: center;
    font-size: 150px;
    line-height: 162px;
    letter-spacing: 3px;
    font-weight: 400;
  }
  .house-illustration {
    position: absolute;
    top: 1210px;
    left: 132px;
    width: 945px;
    height: 780px;
    border-radius: 24px;
    background:
      linear-gradient(180deg, var(--house-grey) 0%, var(--house-grey) 42%, transparent 42%),
      linear-gradient(90deg, var(--buy-red) 0%, var(--buy-red) 45%, var(--sell-blue) 55%, var(--sell-blue) 100%);
    opacity: 0.92;
  }
  .cta-band {
    position: absolute;
    left: 0;
    bottom: 0;
    width: 100%;
    height: 205px;
    background: var(--brand-red);
    display: flex;
    align-items: center;
    justify-content: center;
  }
  .cta-band .cta {
    font-size: 132px;
    letter-spacing: 4px;
    line-height: 1;
  }
</style>
</head>
<body>
  <main class="flyer">
    <header class="brand">
      <div class="brand-square"></div>
      <div class="brand-name">
        <span class="name">dunehill</span>
        <span class="tagline">REAL ESTATE</span>
      </div>
    </header>

    <h1 class="headline">Want to know<br>what's your<br>house is worth</h1>

    <div class="house-illustration" role="img" aria-label="3D white house with a chimney, with large red BUY and blue SELL letters across its front"></div>

    <footer class="cta-band">
      <p class="cta">CONTACT US TODAY</p>
    </footer>
  </main>
</body>
</html>
```